New iOS App design for Boston Startup

We are looking for a new app design for our Zorvak app. The current app's design feels outdated and we like to add lots of new functionality and a new navigation as well. A complete overhaul therefore!
We want you to design 5 screens that will have changed the most. The complete wireframes of these 5 pages are attached in the requirements document.
Once the winning design is selected we will award the winner with the designing all other screens (40-50 screens based on the same design). This will be a separate project worth $1000. The winning designer can get more follow up work if both sides are happy about the cooperation.
We will give feedback as soon as the first screen has been uploaded for review. Final decision will be made only after all 5 screens are finished.
We hope you give it your best!
Note: will only communicate through PixelGuild (no skype),
Updates
Project Deadline Extended
Reason: Want to give designers a chance to submit their designs as I understand from some, the deadline is too close.
I have raised the award and introduced a 2nd price as well to make it worth your time. I hope you give it your best shot.
Project Deadline Extended
Reason: A few of you have asked for an extension of the deadline as time is running out. I will extend by one day. Tell me if you need more.
Industry/Entity Type
Startup
Requirements
Must have
- At least 1 screen before we can give you feedback.
Nice to have
- multiple options of 1 screen to get to a desirable design

```html
<!DOCTYPE html>
<html lang="en">
<head>
<meta charset="utf-8">
<title>Zorvak – Home</title>
<link rel="stylesheet" href="https://fonts.googleapis.com/css2?family=Arimo:wght@400;700&display=swap">
<style>
:root{
  --page:#d9d9d9;
  --navy:#032d48;
  --surface:#f2f2f2;
  --white:#ffffff;
  --ink:#111111;
  --muted:#c4c4c4;
  --rule:#dcdcdc;
  --up:#2f6f12;
  --down:#f07272;
  --step:#1a8fe0;
  --green:#b9e582;
  --sky:#62c8f4;
  --orange:#ffbd63;
  --active:#0bbcf4;
}
*{box-sizing:border-box;margin:0;padding:0}
html,body{width:847px;height:1200px;overflow:hidden}
body{background:var(--page);font-family:"Arimo",Helvetica,Arial,sans-serif;position:relative}
.app{position:absolute;left:93px;top:109px;width:644px;height:964px;background:var(--surface);overflow:hidden}
.header{position:absolute;left:0;top:0;width:100%;height:127px;background:var(--navy);color:var(--white)}
.status{position:absolute;top:8px;left:16px;right:14px;height:26px;font-size:22px;display:flex;align-items:center;justify-content:space-between}
.status__left,.status__right{display:flex;align-items:center;gap:8px}
.status__time{position:absolute;left:50%;transform:translateX(-50%)}
.title{position:absolute;top:64px;width:100%;text-align:center;font-size:32px;font-weight:700}
.menu{position:absolute;left:28px;top:70px}
.score{position:absolute;left:27px;top:141px;width:138px;height:132px;background:var(--white);border:2px solid #e2e2e2;border-radius:8px;text-align:center}
.score__value{font-size:58px;line-height:1;margin-top:10px;color:var(--ink)}
.score__label{font-size:22px;color:var(--muted);margin-top:4px}
.score__delta{font-size:20px;color:var(--down);margin-top:4px}
.stat{position:absolute;top:156px;width:140px;margin-left:-70px;text-align:center}
.stat__value{font-size:24px;color:var(--ink)}
.stat__value em{font-style:normal;color:var(--up);font-size:22px}
.stat__label{font-size:21px;color:var(--muted);margin-top:12px}
.week{position:absolute;left:188px;top:237px;width:430px;height:32px;background:var(--navy);color:var(--white);font-size:21px;font-weight:700;display:flex;align-items:center;justify-content:center}
.week__step{position:absolute;top:0;width:34px;height:32px;background:var(--step);display:flex;align-items:center;justify-content:center}
.week__step--prev{left:0}.week__step--next{right:0}
.divider{position:absolute;left:30px;top:294px;width:588px;height:1px;background:var(--rule)}
.action{position:absolute;left:184px;width:280px;height:68px;border-radius:6px;color:var(--white);font-size:27px;display:flex;align-items:center;padding-left:12px}
.action__chev{position:absolute;right:10px;top:22px}
.action--analytics{top:337px;background:var(--green)}
.action--course{top:455px;background:var(--sky);font-size:24px}
.action--countdown{top:573px;background:var(--orange)}
.action--countdown strong{font-size:31px;margin-right:10px}
.action__icon{margin-right:14px}
.upnext{position:absolute;left:20px;top:666px;font-size:20px;color:var(--muted)}
.lesson{position:absolute;left:20px;top:704px;width:608px;height:87px;background:var(--white);border-top:8px solid var(--rule);border-radius:8px;padding:8px 0 0 16px}
.lesson__num{font-size:20px;font-weight:700;color:var(--ink)}
.lesson__name{font-size:27px;color:var(--ink);margin-left:10px}
.lesson__chev{position:absolute;right:16px;top:30px}
.tabbar{position:absolute;left:0;top:862px;width:100%;height:102px;background:var(--navy);display:flex}
.tab{flex:1;position:relative;color:var(--white);font-size:19px;font-weight:700;text-align:center;padding-top:12px}
.tab svg{display:block;margin:0 auto 6px;height:52px}
.tab--active{background:var(--active);margin-top:-8px;padding-top:20px}
</style>
</head>
<body>
<main class="app">
  <header class="header">
    <div class="status">
      <div class="status__left">
        <svg width="62" height="12" viewBox="0 0 62 12"><g fill="#fff"><circle cx="6" cy="6" r="5"/><circle cx="18" cy="6" r="5"/><circle cx="30" cy="6" r="5"/></g><g fill="none" stroke="#fff" stroke-width="1.3"><circle cx="42" cy="6" r="4.4"/><circle cx="54" cy="6" r="4.4"/></g></svg>
        <span>Nuvela</span>
        <svg width="26" height="20" viewBox="0 0 26 20"><g fill="none" stroke="#fff" stroke-width="3" stroke-linecap="round"><path d="M2 7a16 16 0 0 1 22 0"/><path d="M6 11a10 10 0 0 1 14 0"/></g><circle cx="13" cy="16" r="2.6" fill="#fff"/></svg>
      </div>
      <span class="status__time">23:12</span>
      <div class="status__right">
        <svg width="14" height="22" viewBox="0 0 14 22"><path d="M2 6l10 10-5 5V1l5 5L2 16" fill="none" stroke="#fff" stroke-width="1.8"/></svg>
        <span>100%</span>
        <svg width="48" height="22" viewBox="0 0 48 22"><rect x="1" y="2" width="42" height="18" rx="3" fill="none" stroke="#fff" stroke-width="1.6"/><rect x="4" y="5" width="36" height="12" rx="1" fill="#fff"/><rect x="44" y="8" width="3" height="6" fill="#fff"/></svg>
      </div>
    </div>
    <svg class="menu" width="42" height="30" viewBox="0 0 42 30"><g fill="#fff"><rect y="0" width="42" height="4" rx="2"/><rect y="13" width="42" height="4" rx="2"/><rect y="26" width="42" height="4" rx="2"/></g></svg>
    <h1 class="title">Welcome back, Oren</h1>
  </header>

  <section class="score">
    <div class="score__value">650</div>
    <div class="score__label">SCORE</div>
    <div class="score__delta">&#8595; -18</div>
  </section>

  <div class="stat" style="left:257px"><div class="stat__value">34%<em>&#129045;+10</em></div><div class="stat__label">completion</div></div>
  <div class="stat" style="left:419px"><div class="stat__value">20<em>&#129045;+3</em></div><div class="stat__label">sessions</div></div>
  <div class="stat" style="left:559px"><div class="stat__value">18<em>&#129045;+10</em></div><div class="stat__label">min.</div></div>

  <div class="week">
    <span class="week__step week__step--prev"><svg width="12" height="16" viewBox="0 0 12 16"><path d="M9 2L3 8l6 6" fill="none" stroke="#fff" stroke-width="2.5"/></svg></span>
    this week
    <span class="week__step week__step--next"><svg width="12" height="16" viewBox="0 0 12 16"><path d="M3 2l6 6-6 6" fill="none" stroke="#fff" stroke-width="2.5"/></svg></span>
  </div>

  <div class="divider"></div>

  <a class="action action--analytics">
    <svg class="action__icon" width="28" height="24" viewBox="0 0 28 24"><rect x="1" y="1" width="26" height="22" fill="none" stroke="#fff" stroke-width="1.5"/><path d="M4 18l6-6 4 3 9-9" fill="none" stroke="#fff" stroke-width="1.5"/></svg>
    Analytics
    <svg class="action__chev" width="16" height="24" viewBox="0 0 16 24"><path d="M3 3l9 9-9 9" fill="none" stroke="#fff" stroke-width="3"/></svg>
  </a>
  <a class="action action--course">
    <svg class="action__icon" width="30" height="24" viewBox="0 0 30 24"><g fill="none" stroke="#fff" stroke-width="1.4"><circle cx="3" cy="3" r="2"/><circle cx="3" cy="12" r="2"/><circle cx="3" cy="21" r="2"/><path d="M9 3h20M9 12h20M9 21h20"/></g></svg>
    Course Overview
    <svg class="action__chev" width="16" height="24" viewBox="0 0 16 24"><path d="M3 3l9 9-9 9" fill="none" stroke="#fff" stroke-width="3"/></svg>
  </a>
  <a class="action action--countdown">
    <strong>33</strong> Days until test
    <svg class="action__chev" width="16" height="24" viewBox="0 0 16 24"><path d="M3 3l9 9-9 9" fill="none" stroke="#fff" stroke-width="3"/></svg>
  </a>

  <div class="upnext">Up Next:</div>
  <a class="lesson">
    <div class="lesson__num">Lesson 3</div>
    <div class="lesson__name">Essay Writing</div>
    <svg class="lesson__chev" width="16" height="24" viewBox="0 0 16 24"><path d="M3 3l9 9-9 9" fill="none" stroke="#111" stroke-width="3"/></svg>
  </a>

  <nav class="tabbar">
    <div class="tab"><svg width="46" height="52" viewBox="0 0 46 52"><g fill="none" stroke="#fff" stroke-width="2"><rect x="4" y="2" width="36" height="46"/><path d="M40 6h4v44H8v-2"/><path d="M10 10h24"/></g></svg>Theory</div>
    <div class="tab"><svg width="52" height="52" viewBox="0 0 52 52"><g fill="none" stroke="#fff" stroke-width="2"><path d="M38 4l10 10-30 30H8V34z"/><path d="M32 10l10 10M8 34l10 10"/></g></svg>Practice</div>
    <div class="tab tab--active"><svg width="52" height="48" viewBox="0 0 52 48"><path d="M26 2L2 24h7v22h13V32h8v14h13V24h7L41 18V6h-6v7z" fill="#fff"/></svg>Home</div>
    <div class="tab"><svg width="52" height="52" viewBox="0 0 52 52"><g fill="none" stroke="#fff" stroke-width="2"><circle cx="26" cy="8" r="6"/><path d="M26 14v20"/><rect x="4" y="36" width="44" height="12" rx="2"/><path d="M14 34h8"/></g></svg>Games</div>
    <div class="tab"><svg width="44" height="52" viewBox="0 0 44 52"><g fill="none" stroke="#fff" stroke-width="2"><path d="M4 2h26l10 10v38H4z"/><path d="M30 2v10h10M10 20h24M10 27h24M10 34h24M10 41h24"/></g></svg>Test</div>
  </nav>
</main>
</body>
</html>
```